Business card design needed

Hello, I Need a business card for a company that specialises in providing contract management services for civil construction projects - roads, bridges etc.
I do have a logo that i produced for PLOVER Civilworks however it probably needs a little work, the circles dont have defined edges, i was thinking the colours should reflect the dry interior of Australia progressing out to the colours of the ocean as you move towards the East.... that was my thinking anyway!
Target Market(s)
Professional people generally 30+ yrs old who need professional services to deliver contracts in a high risk environment
Industry/Entity Type
Construction
Contact Information for Business Card
PLOVER Civilworks
Darren Holbeck - Director and Principal Engineer
Registered Professional Engineer of Queensland
Phone 0438 615 272
Email darren@plovercivilworks.com.au
ABN 83 214 570 618
Logo Text
PLOVER Civilworks
Logo styles of interest
Pictorial/Combination Logo
Wordmark Logo
Lettermark Logo
Look and feel

```html
<!DOCTYPE html>
<html lang="en">
<head>
<meta charset="utf-8">
<title>PLOVER Civilworks – Business Card</title>
<link rel="stylesheet" href="https://fonts.googleapis.com/css2?family=Carlito:wght@400;700&display=swap">
<style>
  :root {
    --paper: #ffffff;
    --ink: #000000;
    --red: #c0140c;
    --yellow: #f2dc00;
    --green: #22a37a;
  }
  * { margin: 0; padding: 0; box-sizing: border-box; }
  html, body {
    width: 1200px;
    height: 690px;
    overflow: hidden;
    background: var(--paper);
  }
  .card {
    position: relative;
    width: 1200px;
    height: 690px;
    background: var(--paper);
    font-family: "Carlito", "Calibri", sans-serif;
    color: var(--ink);
  }

  /* Diagonal contact lines */
  .contact-line {
    position: absolute;
    transform-origin: left bottom;
    transform: rotate(-45deg);
    white-space: nowrap;
    font-size: 31px;
    line-height: 1;
    letter-spacing: 0.2px;
  }
  .contact-phone { left: 78px;  top: 468px; color: var(--green); display: flex; align-items: center; gap: 8px; }
  .contact-email { left: 146px; top: 478px; color: var(--red); }
  .contact-abn   { left: 210px; top: 478px; color: var(--yellow); }
  .phone-icon { width: 24px; height: 24px; flex: none; }

  /* Person block */
  .person {
    position: absolute;
    left: 540px;
    top: 326px;
    width: 600px;
    text-align: center;
  }
  .person-name {
    font-size: 42px;
    font-weight: 400;
    line-height: 1.1;
    margin-bottom: 8px;
  }
  .person-role {
    font-size: 28px;
    line-height: 1.35;
  }

  /* Brand name */
  .brand-name {
    position: absolute;
    left: 316px;
    top: 510px;
    font-size: 104px;
    font-weight: 400;
    line-height: 1;
    color: var(--ink);
    white-space: nowrap;
  }
</style>
</head>
<body>
  <main class="card">
    <div class="contact-line contact-phone">
      <svg class="phone-icon" viewBox="0 0 24 24" aria-hidden="true">
        <path d="M6.6 3.2c.7-.5 1.6-.3 2 .4l1.7 3c.4.7.2 1.5-.4 2l-1.2.9c1 2.3 2.9 4.3 5.2 5.4l1-1.1c.5-.6 1.4-.7 2-.3l2.9 1.8c.7.4.9 1.3.4 2l-1 1.4c-.8 1.1-2.2 1.6-3.5 1.2C10 18.4 5.5 13.9 4 8.4c-.4-1.3.1-2.7 1.2-3.5z" fill="var(--green)"/>
      </svg>
      <span>0438 615 272</span>
    </div>
    <div class="contact-line contact-email">darren@plovercivilworks.com.au</div>
    <div class="contact-line contact-abn">ABN 83 214 570 618</div>

    <section class="person">
      <h1 class="person-name">Darren Holbeck</h1>
      <p class="person-role">Director and Principal Engineer Registered</p>
      <p class="person-role">Professional Engineer of Queensland</p>
    </section>

    <div class="brand-name">PLOVER Civilworks</div>
  </main>
</body>
</html>
```